Briefbogen und Visitenkarte für Grundstücksverwaltunggesellschaft
Zielgruppe
Wir sind eine Grundstücksverwaltungsgesellschaft und Verwalten eine Vielzahl an Logistik- und Industrieimmobilien.
Aufgabenstellung
Wir bitten um Verwendung unseres Logo, siehe Anlage. Die Bildmarke darf nicht verändert werden, die Wortmarke darf unter Umständen otimiert werden.
Wir möchten einen dezenten Auftritt vermitteln und bitten daher um graue Schrift als Grundfarbe.
Bei der Visitenkarte könnten wir uns eine einfarbig blaue Rückseite vorstellen.
Folgende Daten kommen zur Verwendung:
Lindquell Grundstücksverwaltungs GmbH
Internet: www.lindquell-grundstuecksverwaltung.example

```html
<!DOCTYPE html>
<html lang="de">
<head>
<meta charset="utf-8">
<title>Lindquell Grundstücksverwaltungs GmbH – Geschäftsausstattung</title>
<link rel="stylesheet" href="https://fonts.googleapis.com/css2?family=Source+Sans+3:wght@400;600&display=swap">
<style>
:root{
  --stage:#c89e69;
  --paper:#ffffff;
  --brand-blue:#004f80;
  --text-grey:#6f6f6f;
  --mark-grey:#8a8a8a;
  --line-grey:#b5b5b5;
  --shadow:rgba(40,25,10,.45);
}
*{box-sizing:border-box;margin:0;padding:0}
html,body{width:1200px;height:990px;overflow:hidden;background:var(--stage)}
body{position:relative;font-family:"Source Sans 3",sans-serif;color:var(--text-grey)}

.sheet{position:absolute;background:var(--paper);box-shadow:10px 10px 12px var(--shadow)}

/* Briefbogen */
.letterhead{left:43px;top:50px;width:630px;height:891px}
.letterhead .top-bar{position:absolute;left:0;top:37px;width:340px;height:24px;background:var(--brand-blue)}
.brand{position:absolute;display:flex;align-items:center;gap:8px}
.brand .square{width:16px;height:16px;background:var(--mark-grey);flex:none}
.brand .name{color:var(--mark-grey);font-weight:400;line-height:1.2;letter-spacing:.04em}
.letterhead .brand{left:359px;top:38px}
.letterhead .brand .name{font-size:14px}
.contact{position:absolute;left:429px;top:82px;font-size:8px;line-height:10.3px}
.contact dl{display:grid;grid-template-columns:32px auto;margin-top:10px}
.contact dt{color:var(--brand-blue)}
.contact dl.web{grid-template-columns:33px auto}
.sender-line{position:absolute;left:73px;top:216px;font-size:5.4px;white-space:nowrap}
.fold-mark{position:absolute;left:14px;width:16px;height:1px;background:#555}
.fold-mark.first{top:304px}
.fold-mark.second{top:585px}
.letter-footer{position:absolute;left:0;right:0;top:839px;height:42px;border-top:1.5px solid var(--brand-blue);border-bottom:3px solid var(--brand-blue)}
.letter-footer .brand{left:18px;top:13px;gap:10px}
.letter-footer .brand .square{width:14px;height:14px}
.letter-footer .brand .name{font-size:8px}
.footer-col{position:absolute;font-size:6px;line-height:7.2px}
.footer-col .label{color:var(--brand-blue)}
.footer-col.bank{left:309px;top:4px}
.footer-col.register{left:490px;top:8px}

/* Umschläge */
.envelope{width:662px;height:331px}
.envelope-back{left:499px;top:350px}
.envelope-back .flap{position:absolute;left:0;top:0;width:662px;height:78px}
.envelope-back .flap-name{position:absolute;left:0;right:0;top:28px;text-align:center;color:#fff;font-size:13px;letter-spacing:.06em}
.envelope-front{left:469px;top:501px;width:660px}
.envelope-front .brand{left:55px;top:36px;gap:12px}
.envelope-front .brand .square{width:22px;height:22px}
.envelope-front .brand .name{font-size:17px}
.envelope-front .sender{position:absolute;left:115px;top:82px;font-size:9.5px;letter-spacing:.02em}
.envelope-front .window{position:absolute;left:48px;top:179px;width:279px;height:110px;border:1px solid var(--line-grey);border-radius:14px}
.envelope-front .address-band{position:absolute;left:0;right:0;top:307px;height:24px;background:var(--brand-blue);color:#fff;font-size:12.5px;line-height:24px;padding-left:434px}
</style>
</head>
<body>

<section class="sheet letterhead" aria-label="Briefbogen">
  <div class="top-bar"></div>
  <div class="brand">
    <span class="square"></span>
    <span class="name">Lindquell<br>Grundstücksverwaltungs GmbH</span>
  </div>
  <div class="contact">
    <p>Ahornstraße 9<br>23570 Musterhafen</p>
    <dl>
      <dt>Telefon:</dt><dd>0451 555010-0</dd>
      <dt>Telefax:</dt><dd>0451 555010-33</dd>
      <dt>Mobil:</dt><dd>0170 5550199 (nur auf VK)</dd>
    </dl>
    <dl class="web">
      <dt>Internet:</dt><dd>www.lindquell-grundstuecksverwaltung.example</dd>
      <dt>Mail:</dt><dd>info@lindquell-grundstuecksverwaltung.example</dd>
    </dl>
  </div>
  <p class="sender-line">Lindquell Grundstücksverwaltungs GmbH • Ahornstraße 9 • 23570 Musterhafen</p>
  <span class="fold-mark first"></span>
  <span class="fold-mark second"></span>
  <footer class="letter-footer">
    <div class="brand">
      <span class="square"></span>
      <span class="name">Lindquell Grundstücksverwaltungs GmbH</span>
    </div>
    <div class="footer-col bank">
      <p class="label">Bankverbindung:</p>
      <p>Sparkasse Musterhafen AG</p>
      <p>IBAN:&nbsp; DE00 1234 5678 9012 3456 78</p>
      <p>BIC:&nbsp;&nbsp;&nbsp;&nbsp; MUSTDEXXXXX</p>
    </div>
    <div class="footer-col register">
      <p>USt.IDNr.: DE000000000</p>
      <p>Steuernummer: 00 000 00000</p>
      <p>Amtsgericht Musterhafen, HRB 0000 MH</p>
    </div>
  </footer>
</section>

<section class="sheet envelope envelope-back" aria-label="Umschlag Rückseite">
  <svg class="flap" viewBox="0 0 662 78" aria-hidden="true">
    <path d="M0 0 H662 L630 58 Q619 78 596 78 H94 Q72 78 58 62 Z" fill="var(--brand-blue)"/>
  </svg>
  <p class="flap-name">Lindquell</p>
</section>

<section class="sheet envelope envelope-front" aria-label="Umschlag Vorderseite">
  <div class="brand">
    <span class="square"></span>
    <span class="name">Lindquell<br>Grundstücksverwaltungs GmbH</span>
  </div>
  <p class="sender">Ahornstraße 9 • 23570 Musterhafen</p>
  <div class="window"></div>
  <div class="address-band">Ahornstraße 9 • 23570 Musterhafen</div>
</section>

</body>
</html>
```